Informational Site for Advanced Chemistry R&D

The company develops oxidation chemistry for air, water, fuel pollution controls. The site has been prototyped at www.velmirlab.net. Take a look. Now, the task is to design it for eye-catching beauty with use of color, on-page scroll-driven color transition and parallax effects. Should capture the themes: high technology, wow it's beautiful, modern, uncluttered, clean urban environment.

Target Market(s)

China Environmentally Conscious Government and Industry,

Industry/Entity Type

It Company

Number of Pages Required

3 page

Font styles to use
Sans Serif

Requirements
Must have
• Parallax effects, desktop compatible, Rich, Modern, Simple, Graphic
Nice to have
• Mobile Phone Compatible
Should not have
• Flash, or anything that is slow to load or requires high bandwidth

```html
<!DOCTYPE html>
<html lang="en">
<head>
<meta charset="utf-8">
<title>Velmir Lab – Advanced Oxidation</title>
<link rel="stylesheet" href="https://fonts.googleapis.com/css2?family=Montserrat:wght@400;600;700&family=Open+Sans:wght@400;600&display=swap">
<style>
:root{
  --blue:#1a6fb8;
  --blue-dark:#145a98;
  --teal:#2fb9b2;
  --teal-light:#4cc8c0;
  --ink:#333;
  --grey:#777;
  --footer:#262626;
  --footer-line:#3a3a3a;
  --white:#fff;
}
*{box-sizing:border-box;margin:0;padding:0}
html,body{width:1200px;height:2782px;overflow:hidden}
body{position:relative;font-family:"Open Sans",Arial,sans-serif;color:var(--ink);background:var(--white)}
.abs{position:absolute}
.btn{position:absolute;display:flex;align-items:center;justify-content:center;border-radius:20px;font-size:14px;background:var(--blue);color:var(--white);font-family:"Open Sans",sans-serif}
.heading{font-family:"Montserrat",sans-serif;font-weight:700}

/* hero */
.hero{left:0;top:0;width:1200px;height:600px;background:linear-gradient(180deg,#2f5f96 0%,#5c86b4 35%,#89a6c4 55%,#3f6a99 75%,#244c7c 100%)}
.hero-wave{left:0;top:540px;width:1200px;height:62px}
.brand-box{left:145px;top:0;width:125px;height:80px;background:var(--white);display:flex;align-items:center;justify-content:center;gap:6px;font-family:"Montserrat",sans-serif;font-weight:600;font-size:15px;color:var(--blue)}
.brand-box .dot{width:12px;height:12px;border-radius:50%;background:var(--teal)}
.nav{top:27px;left:0;width:1200px;height:30px;font-size:15px;color:var(--white);font-family:"Montserrat",sans-serif}
.nav span{position:absolute;top:5px}
.nav .active{top:0;left:592px;width:78px;height:30px;border:2px solid var(--white);border-radius:16px;display:flex;align-items:center;justify-content:center}
.hero-title{top:288px;width:1200px;text-align:center;font-size:58px;color:var(--white)}
.hero-sub{top:352px;width:1200px;text-align:center;font-family:"Montserrat",sans-serif;font-size:31px;color:var(--white)}
.hero-tag{top:445px;width:1200px;text-align:center;font-size:13px;color:var(--white)}
.scroll-cue{left:583px;top:535px;width:34px;height:34px}

/* intro */
.diagram{left:185px;top:640px;width:325px;height:362px;background:radial-gradient(circle at 50% 50%,#f7d34a 0 8%,#fff7d6 9% 45%,#ffffff 70%)}
.intro-title{left:599px;top:660px;font-size:26px;color:var(--blue)}
.intro-text{left:599px;top:703px;width:455px;font-size:14.5px;line-height:24px;color:var(--grey)}
.intro-list{left:599px;top:797px;font-size:16px;line-height:29px;color:var(--ink);list-style:none}
.intro-list li::before{content:"•";margin-right:12px}
.intro-text.second{top:875px}

/* feature band */
.feature{left:0;top:1072px;width:1200px;height:368px;background:linear-gradient(180deg,#262a36 0%,#5a3f3a 35%,#3b3f4d 65%,#2c3140 100%)}
.pitch{left:145px;top:1139px;width:419px;height:226px;background:var(--blue)}
.pitch p{position:absolute;left:30px;top:22px;width:360px;font-family:"Montserrat",sans-serif;font-size:24px;line-height:31px;color:var(--white)}
.pitch .btn{left:28px;top:158px;width:126px;height:32px;background:var(--white);color:var(--blue)}
.solutions{left:634px;top:1139px;width:420px;height:226px;background:var(--teal)}
.solutions h3{position:absolute;left:32px;top:20px;font-family:"Montserrat",sans-serif;font-weight:400;font-size:24px;color:var(--white)}
.tile{position:absolute;top:70px;width:107px;height:104px;border:1.5px solid rgba(255,255,255,.8);display:flex;flex-direction:column;align-items:center;justify-content:flex-end;padding-bottom:14px;gap:12px;font-family:"Montserrat",sans-serif;font-size:16px;color:var(--white)}
.tile.on{background:var(--white);color:var(--teal)}
.partner-tag{left:564px;top:1415px;width:198px;height:25px;background:var(--white);font-size:11px;display:flex;align-items:center;justify-content:center;color:var(--ink)}

/* partners */
.partners-label{left:143px;top:1480px;font-family:"Montserrat",sans-serif;font-size:21px;line-height:25px;color:var(--blue)}
.partners-rule{left:291px;top:1470px;width:1px;height:64px;background:#ddd}
.badge{position:absolute;top:1466px;width:72px;height:72px;border-radius:50%}

/* solutions grid */
.grid-band{left:0;top:1562px;width:1200px;height:475px;background:linear-gradient(180deg,#46c3bd 0%,#2ba7a5 45%,#1f8b8b 100%)}
.grid-title{top:1623px;width:1200px;text-align:center;font-size:25px;color:var(--white)}
.card{position:absolute;top:1688px;width:224px;height:275px;background:var(--white)}
.card .photo{height:128px}
.card .arrow{position:absolute;left:95px;top:111px;width:34px;height:34px}
.card h4{position:absolute;top:153px;width:100%;text-align:center;font-family:"Montserrat",sans-serif;font-weight:600;font-size:15px;color:#222}
.card p{position:absolute;top:180px;left:18px;width:188px;text-align:center;font-size:10px;line-height:14px;color:var(--grey)}

/* about */
.about-title{top:2082px;width:1200px;text-align:center;font-size:25px;color:var(--blue)}
.about-photo{left:200px;top:2155px;width:377px;height:232px;border:3px solid var(--white);box-shadow:0 0 0 1px #ddd;background:linear-gradient(160deg,#7a6a5a 0%,#3d3b38 45%,#8b7d6b 75%,#2d2c2a 100%)}
.about-sub{left:621px;top:2142px;font-size:20px;color:var(--teal)}
.about-text{left:621px;top:2178px;width:410px;font-size:13.5px;line-height:24px;color:#555}
.about-text .cap{font-size:26px;color:var(--blue);font-family:"Montserrat",sans-serif;margin-right:2px}

/* footer */
.footer{left:0;top:2467px;width:1200px;height:315px;background:var(--footer);color:#cfcfcf}
.footer h5{position:absolute;top:50px;font-family:"Montserrat",sans-serif;font-size:17px;color:var(--teal)}
.footer ul{position:absolute;list-style:none;font-size:11.5px}
.sitemap{left:143px;top:88px;line-height:28px}
.contact{left:332px;top:86px;width:210px}
.contact li{position:relative;padding-left:26px;margin-bottom:8px;line-height:17px;font-size:12.5px}
.contact svg{position:absolute;left:0;top:2px}
.follow{left:594px;top:96px}
.follow li{display:flex;align-items:center;gap:10px;height:32px;font-size:12px}
.follow .ring{width:24px;height:24px;border-radius:50%;border:1.5px solid #bbb}
.footer-mark{left:825px;top:185px;font-family:"Montserrat",sans-serif;font-weight:700;font-size:46px;color:#3e3e3e}
.footer-rule{left:0;top:251px;width:1200px;height:1px;background:var(--footer-line)}
.copyright{top:270px;width:1200px;text-align:center;font-size:11px;color:#aaa}
</style>
</head>
<body>

<section class="abs hero" role="img" aria-label="City skyline reflected in a river under a blue sky"></section>
<svg class="abs hero-wave" viewBox="0 0 1200 62" preserveAspectRatio="none"><path d="M0 40 Q600 -20 1200 40 L1200 62 L0 62 Z" fill="#fff"/></svg>

<div class="abs brand-box"><span class="dot"></span>VelmirLab</div>
<nav class="abs nav">
  <span class="active">Home</span>
  <span style="left:697px">About us</span>
  <span style="left:796px">Technology</span>
  <span style="left:910px">Products</span>
  <span style="left:1007px">Contact</span>
</nav>
<h1 class="abs heading hero-title">Advanced Oxidation</h1>
<p class="abs hero-sub">Science for Environmental Pollution Management</p>
<a class="btn" style="left:536px;top:410px;width:139px;height:30px">Read More</a>
<p class="abs hero-tag">New Ideas For A Cleaner World</p>
<svg class="abs scroll-cue" viewBox="0 0 34 34"><circle cx="17" cy="17" r="15.5" fill="none" stroke="#fff" stroke-width="2"/><path d="M11 14 L17 20 L23 14" fill="none" stroke="#fff" stroke-width="2.2"/></svg>

<div class="abs diagram" role="img" aria-label="Reaction diagram of the hydroxyl radical converting pollutant molecules"></div>
<h2 class="abs heading intro-title">Advanced Oxidation</h2>
<p class="abs intro-text">Advanced Oxidation refers to a variety of techniques employing the Hydroxyl Radical, an energetic, highly reactive cousin of the water molecule:</p>
<ul class="abs intro-list">
  <li>To add oxygen to inorganic molecules</li>
  <li>To remove hydrogen from organic molecules</li>
</ul>
<p class="abs intro-text second">These transformations convert important industrial contaminants into reactive forms that can be captured or that disintegrate into harmless end products.</p>
<a class="btn" style="left:599px;top:963px;width:126px;height:32px">Read More</a>

<section class="abs feature" role="img" aria-label="Blurred industrial plant at dusk"></section>
<div class="abs pitch">
  <p>Environmental pollution control solutions employing nature's most reactive Free Radical</p>
  <a class="btn">Read More</a>
</div>
<div class="abs solutions">
  <h3>Solutions :</h3>
  <div class="tile" style="left:34px">
    <svg width="22" height="30" viewBox="0 0 22 30"><path d="M11 1 C11 1 1 14 1 20 A10 10 0 0 0 21 20 C21 14 11 1 11 1Z" fill="#fff"/></svg>WATER</div>
  <div class="tile on" style="left:156px">
    <svg width="34" height="30" viewBox="0 0 34 30"><path d="M4 2 V28 M4 4 H28 L24 10 L28 16 H4" fill="none" stroke="#2fb9b2" stroke-width="2"/></svg>AIR</div>
  <div class="tile" style="left:279px">
    <svg width="22" height="30" viewBox="0 0 22 30"><rect x="2" y="2" width="18" height="26" rx="4" fill="none" stroke="#fff" stroke-width="2"/><path d="M2 9 H20" stroke="#fff" stroke-width="2"/></svg>FUEL</div>
</div>
<div class="abs partner-tag">Our technology partner in China</div>

<p class="abs partners-label">OUR<br>PARTNERS</p>
<div class="abs partners-rule"></div>
<span class="badge" style="left:329px;background:#1e8ac4"></span>
<span class="badge" style="left:446px;background:#d9412a"></span>
<span class="badge" style="left:554px;background:#2c5aa0"></span>
<span class="badge" style="left:650px;background:#1e8ac4"></span>
<span class="badge" style="left:765px;background:#d9412a"></span>
<span class="badge" style="left:873px;background:#2c5aa0"></span>
<span class="badge" style="left:982px;background:#b3263a"></span>

<section class="abs grid-band"></section>
<h2 class="abs heading grid-title">Our Solutions</h2>
<article class="card" style="left:141px">
  <div class="photo" role="img" aria-label="Refinery towers and pipework" style="background:linear-gradient(180deg,#8a8f96,#3f4349)"></div>
  <svg class="arrow" viewBox="0 0 34 34"><circle cx="17" cy="17" r="17" fill="#1a6fb8"/><path d="M10 17 H23 M18 12 L23 17 L18 22" fill="none" stroke="#fff" stroke-width="2"/></svg>
  <h4>Fuel Oil Desulfurization</h4>
  <p>Our proprietary low temperature and pressure advanced oxidation catalytic process reliably removes sulfur from diesel transportation fuel at less than half the operating ..</p>
</article>
<article class="card" style="left:373px">
  <div class="photo" role="img" aria-label="Worker handling chemical tanks" style="background:linear-gradient(180deg,#6f8aa3,#9a8c75)"></div>
  <svg class="arrow" viewBox="0 0 34 34"><circle cx="17" cy="17" r="17" fill="#1a6fb8"/><path d="M10 17 H23 M18 12 L23 17 L18 22" fill="none" stroke="#fff" stroke-width="2"/></svg>
  <h4>Volatile Organic Compunds</h4>
  <p>Alkanes, alkenes, halogenated hydrocarbons, aromatic hydrocarbons, esters, aldehydes, polycyclic aromatic hydrocarbons. We convert these</p>
</article>
<article class="card" style="left:605px">
  <div class="photo" role="img" aria-label="Smokestacks releasing flue gas" style="background:linear-gradient(180deg,#4a4a5e,#7a6e78)"></div>
  <svg class="arrow" viewBox="0 0 34 34"><circle cx="17" cy="17" r="17" fill="#1a6fb8"/><path d="M10 17 H23 M18 12 L23 17 L18 22" fill="none" stroke="#fff" stroke-width="2"/></svg>
  <h4>Flue Gas Scrubbing</h4>
  <p>Desulfurization and denitrification using our proprietary flue gas advanced oxidation catalytic process (FGAOC). Sulfur and nitrogen are oxidized and adsorbed</p>
</article>
<article class="card" style="left:838px">
  <div class="photo" role="img" aria-label="Wastewater outflow pipe" style="background:linear-gradient(180deg,#7a8a5e,#8d6e43)"></div>
  <svg class="arrow" viewBox="0 0 34 34"><circle cx="17" cy="17" r="17" fill="#1a6fb8"/><path d="M10 17 H23 M18 12 L23 17 L18 22" fill="none" stroke="#fff" stroke-width="2"/></svg>
  <h4>Wastewater Treatment</h4>
  <p>Photoelectrocatalysed (PEC) anodic oxidation removes soluble organics. Novel anode design using our proprietary nano-carbon surface operates non-selectively</p>
</article>

<h2 class="abs heading about-title">About Velmir Lab</h2>
<div class="abs about-photo" role="img" aria-label="Industrial treatment equipment on site"></div>
<h3 class="abs heading about-sub">LET'S TALK ABOUT US</h3>
<p class="abs about-text"><span class="cap">V</span>elmir Lab develops advanced oxidation technologies and materials, which it licenses to Korvane Systems, China. Korvane Systems is engaged in the sales, service and support of environmental solutions for industry and government. With offices in Shanghai, Beijing, Shijiazhuang, and Chengdu, Korvane Systems is among the most advanced and rapidly growing companies offering solutions for air, water and fuel environmental..</p>
<a class="btn" style="left:621px;top:2354px;width:108px;height:30px">Read More</a>

<footer class="abs footer">
  <h5 style="left:143px">Site Map</h5>
  <ul class="sitemap"><li>Home</li><li>About us</li><li>Technology</li><li>Products</li><li>Contact</li></ul>
  <h5 style="left:332px">Contact Us</h5>
  <ul class="contact">
    <li><svg width="12" height="16" viewBox="0 0 12 16"><path d="M6 0 A6 6 0 0 1 12 6 C12 10 6 16 6 16 C6 16 0 10 0 6 A6 6 0 0 1 6 0Z" fill="#ccc"/><circle cx="6" cy="6" r="2.2" fill="#262626"/></svg>Velmir Lab Corporation Harbor Point, U.S.A.</li>
    <li><svg width="13" height="10" viewBox="0 0 13 10"><rect width="13" height="10" fill="#ccc"/><path d="M0 0 L6.5 5 L13 0" fill="none" stroke="#262626"/></svg>info@velmirlab.net</li>
    <li><svg width="12" height="12" viewBox="0 0 12 12"><path d="M2 0 L4.5 3 L3 4.5 C4 7 5 8 7.5 9 L9 7.5 L12 10 L10 12 C4 11 1 8 0 2Z" fill="#ccc"/></svg>Call us: +1 555 014 2290</li>
    <li><svg width="13" height="12" viewBox="0 0 13 12"><rect x="3" y="0" width="7" height="4" fill="#ccc"/><rect x="0" y="5" width="13" height="7" fill="#ccc"/></svg>Fax: 555-017-3301</li>
  </ul>
  <h5 style="left:594px">Follow Us</h5>
  <ul class="follow">
    <li><span class="ring"></span>Fan us on Fanpage</li>
    <li><span class="ring"></span>Follow us on Chirper</li>
    <li><span class="ring"></span>Fan us on Linkwork</li>
    <li><span class="ring"></span>Join in to ViewTube</li>
  </ul>
  <div class="abs footer-mark">VelmirLab</div>
  <div class="abs footer-rule"></div>
  <p class="abs copyright">Copyright velmirlab.net © 2006. All rights reserved</p>
</footer>

</body>
</html>
```